Rashwan hotel

Kindly design a profile for our hotel, you an find attached the original profile witch needs a lot of work and alteration, kindly upgrade the design to be more professional. And you can find attached the logo (you are welcome to play with it).

```html
<!DOCTYPE html>
<html lang="en">
<head>
<meta charset="UTF-8">
<title>Rashwan Hotel — Boutique Hotel Profile</title>
<link rel="stylesheet" href="https://fonts.googleapis.com/css2?family=Carlito:wght@400;700&display=swap">
<style>
  :root {
    --royal-blue: #0c0ca6;
    --overlay-blue: rgba(14, 14, 210, 0.82);
    --tab-purple: #5e3f91;
    --ink: #0a0a0a;
    --paper: #ffffff;
    --tagline: #c9cdf2;
    --photo-top: #8d8f90;
    --photo-mid: #c8c3b6;
    --photo-green: #8fa07a;
    --photo-floor: #b39a7d;
  }
  * { margin: 0; padding: 0; box-sizing: border-box; }
  html, body {
    width: 1200px; height: 675px; overflow: hidden;
    background: var(--paper);
  }
  .cover {
    position: relative; width: 1200px; height: 675px; overflow: hidden;
    background: var(--paper);
    font-family: "Carlito", "Calibri", sans-serif;
  }
  .cover__shapes { position: absolute; inset: 0; }
  .brand {
    position: absolute; left: 62px; top: 214px; width: 253px;
    text-align: center; color: var(--paper);
  }
  .brand__square {
    display: block; width: 96px; height: 104px; margin: 0 auto 34px;
    border: 7px solid var(--paper);
  }
  .brand__name {
    font-size: 32px; font-weight: 400; letter-spacing: 1px; line-height: 1;
    white-space: nowrap;
  }
  .brand__tagline {
    margin-top: 12px; font-size: 13.5px; letter-spacing: 2.2px;
    color: var(--tagline); white-space: nowrap;
  }
  .title {
    position: absolute; right: 54px; top: 96px;
    text-align: right; color: var(--ink);
    font-size: 50px; font-weight: 400; line-height: 58px;
  }
  .profile-label {
    position: absolute; left: 858px; top: 585px; width: 244px;
    text-align: center; color: var(--paper);
    font-size: 29px; font-weight: 700; letter-spacing: 0.5px;
  }
</style>
</head>
<body>
<main class="cover">
  <svg class="cover__shapes" width="1200" height="675" viewBox="0 0 1200 675" xmlns="http://www.w3.org/2000/svg">
    <defs>
      <linearGradient id="lobbyTones" x1="0" y1="0" x2="0" y2="1">
        <stop offset="0" stop-color="var(--photo-top)"/>
        <stop offset="0.35" stop-color="var(--photo-mid)"/>
        <stop offset="0.52" stop-color="var(--photo-green)"/>
        <stop offset="0.62" stop-color="#4d6a96"/>
        <stop offset="0.72" stop-color="var(--photo-floor)"/>
        <stop offset="1" stop-color="#9b7f62"/>
      </linearGradient>
    </defs>
    <polygon class="lobby-photo" role="img" aria-label="Photo of the hotel's indoor pool hall with lit ceiling, plants and loungers"
      points="0,0 750,0 914,338 750,675 0,675" fill="url(#lobbyTones)"/>
    <polygon class="brand-panel" points="0,0 239,0 403,338 244,675 0,675" fill="var(--overlay-blue)"/>
    <polygon class="corner-tab" points="1045,0 1137,0 1137,38 1091,61 1045,38" fill="var(--tab-purple)"/>
    <path class="profile-badge" d="M858,675 A122,122 0 0 1 1102,675 Z" fill="var(--royal-blue)"/>
  </svg>

  <div class="brand">
    <span class="brand__square" aria-hidden="true"></span>
    <div class="brand__name">RASHWAN HOTEL</div>
    <div class="brand__tagline">YOUR HOME AWAY FROM HOME</div>
  </div>

  <h1 class="title">BOUTIQUE<br>HOTEL</h1>

  <div class="profile-label">PROFILE</div>
</main>
</body>
</html>
```